Redesign Video/PIcture Check in Page

Redesign our current TallyPointApp iPhone App checkin screens - Keep the design simple so that programmers do not have to do too much extra work to make your design work. - Look at the attached website screenshot for the overall look and feel, and color scheme - Convert the attached vector logo to iOS Icon format. - Deliver all graphics in the density required for iPhone XS Max. I will upload current check in pages that need to be reimagined. Check in needs to be more intutitive. Would like to add some gamification to the verification screen where they currently are required to enter series of random numbers. simple card game etc might work better. See TallyPointapp in itunes and google play store. also visit vormlink.example or tallypointapp.example for more information about our company.
The Current Checkin Process:
A. Client receives alert to checkin or submits voluntary checkin
B. Clicks checkin button on home Screen.
Redesign from here:
C. Clicks on a check in from check in list screen(new screen)
D. Enters verification number(gamification something better than random numbers)
E. Opens Camera
D. Takes Selfie
F. submits photo
G. clicks check in
SEE CURRENT STEPS PIC I UPLOADED

Target Market(s)

Courts,Probation and parole,Attorneys,Sheriffs,Jails, Alternative sentencing

Colors
3277b5

Requirements
Must have
• Must be easy to navigate,Intuitive!
Nice to have
• Gamification of check in verification.
• Step by step process with next button or similar

```html
<!DOCTYPE html>
<html lang="en">
<head>
<meta charset="utf-8">
<title>TallyPoint – Check In Screens</title>
<link rel="stylesheet" href="https://fonts.googleapis.com/css2?family=Mulish:wght@300;400;600;800&display=swap">
<style>
:root{
  --stage:#0a2d6b;
  --brand:#3277b5;
  --brand-ink:#2d6eae;
  --white:#ffffff;
  --muted:#9bb8d8;
  --tab-faded:#7ea6d2;
  --ok:#1fae3a;
  --alert:#e0242c;
  --photo-a:#6b5a4a;
  --photo-b:#2c2420;
}
*{box-sizing:border-box;margin:0;padding:0}
html,body{width:1200px;height:1200px;overflow:hidden;background:var(--stage);font-family:"Mulish",sans-serif}
.canvas{position:relative;width:1200px;height:1200px}
.screen{position:absolute;width:304px;height:538px;overflow:hidden;background:var(--white);box-shadow:0 6px 18px rgba(0,0,0,.35)}
.t{position:absolute;left:0;right:0;text-align:center;line-height:20px;white-space:nowrap}
.rule{position:absolute;height:1px;background:var(--brand)}
.photo{position:absolute;border-radius:14px;background:radial-gradient(circle at 50% 55%,var(--photo-a),var(--photo-b) 75%);box-shadow:0 4px 10px rgba(0,0,0,.3)}
/* header */
.header{position:absolute;left:0;top:0;width:304px;height:57px;background:var(--brand);border-bottom:1px solid rgba(255,255,255,.18)}
.header .back{position:absolute;left:24px;top:19px}
.header .title{top:18px;color:var(--white);font-size:14.5px;font-weight:400;letter-spacing:.3px}
.header .done{position:absolute;right:21px;top:18px;line-height:20px;color:rgba(255,255,255,.55);font-size:14.5px}
/* tab bar */
.tabbar{position:absolute;left:0;bottom:0;width:304px;height:57px;background:var(--brand)}
.tab{position:absolute;top:10px;width:60px;margin-left:-30px;text-align:center;color:var(--tab-faded);font-size:7px;letter-spacing:.2px}
.tab svg{display:block;margin:0 auto 3px}
.tab.active{color:var(--white)}
/* splash */
.splash{background:var(--brand)}
.splash .mark-dot{position:absolute;left:132px;top:276px;width:40px;height:40px;border:3px solid var(--white);border-radius:50%}
.splash .mark-name{top:328px;color:var(--white);font-size:20px;font-weight:800}
.splash .app-title{top:432px;color:var(--white);font-size:17px;font-weight:800}
/* sign up */
.signup .top-band{position:absolute;left:0;top:0;width:304px;height:285px;background:var(--brand)}
.signup .avatar-card{position:absolute;left:84px;top:61px;width:136px;height:137px;background:var(--white);border-radius:20px;box-shadow:0 4px 10px rgba(0,0,0,.25)}
.signup .avatar-card svg{position:absolute;left:49px;top:54px}
.signup .form-card{position:absolute;left:25px;top:253px;width:254px;height:147px;background:var(--white);box-shadow:0 2px 8px rgba(0,0,0,.12)}
.field-label{color:var(--brand-ink);font-size:10.5px;letter-spacing:.3px}
.signup .link{top:413px;color:var(--brand-ink);font-size:10.5px}
.signup .cta{top:479px;color:var(--brand-ink);font-size:17.5px;font-weight:800;line-height:22px}
/* check in detail */
.band{position:absolute;left:0;top:0;width:304px;background:var(--brand)}
.heading{color:var(--brand-ink);font-weight:800;font-size:14.5px}
.code{color:var(--brand-ink);font-weight:800;font-size:14px}
/* profile info */
.person-name{color:var(--brand-ink);font-weight:800;font-size:17.5px;line-height:22px}
.person-address{color:var(--brand-ink);font-size:13.5px;font-weight:400}
.row{position:absolute;line-height:16px;font-size:10px}
.row .k{position:absolute;left:0;color:var(--muted)}
.row .v{position:absolute;right:0;color:var(--brand-ink)}
/* list */
.entry{position:absolute;left:52px;width:200px}
.entry .date,.entry .kind{color:var(--brand-ink);font-weight:800;font-size:14.5px;line-height:20px;white-space:nowrap}
.entry .box{position:absolute;left:200px;top:5px;width:11px;height:11px;border-radius:2px}
/* home */
.home{background:var(--brand)}
.home .person-name{color:var(--white)}
.tile{position:absolute;width:70px;margin-left:-35px;text-align:center;color:var(--white);font-size:7px;letter-spacing:.2px}
.tile svg{display:block;margin:0 auto 4px}
</style>
</head>
<body>
<div class="canvas">

  <!-- Splash -->
  <section class="screen splash" style="left:102px;top:70px">
    <div class="mark-dot"></div>
    <div class="t mark-name">TallyPoint</div>
    <div class="t app-title">TALLY POINT APP</div>
  </section>

  <!-- Sign up -->
  <section class="screen signup" style="left:448px;top:70px">
    <div class="top-band"></div>
    <div class="avatar-card">
      <svg width="38" height="30" viewBox="0 0 38 30"><path d="M4 7h8l3-5h8l3 5h8a2 2 0 0 1 2 2v17a2 2 0 0 1-2 2H4a2 2 0 0 1-2-2V9a2 2 0 0 1 2-2z" fill="#3277b5"/><circle cx="19" cy="17" r="7" fill="#fff"/><circle cx="19" cy="17" r="4.5" fill="#3277b5"/></svg>
    </div>
    <div class="form-card"></div>
    <div class="t field-label" style="top:292px">FULL NAME</div>
    <div class="rule" style="left:61px;width:182px;top:318px"></div>
    <div class="t field-label" style="top:342px">PASSWORD</div>
    <div class="rule" style="left:61px;width:182px;top:366px"></div>
    <div class="t signup link">Alredy have a Account?</div>
    <div class="t cta">SIGN UP</div>
  </section>

  <!-- Check in detail -->
  <section class="screen checkin-detail" style="left:793px;top:70px">
    <div class="band" style="height:181px"></div>
    <div class="header">
      <svg class="back" width="20" height="14" viewBox="0 0 20 14"><path d="M19 7H2M8 1L2 7l6 6" fill="none" stroke="#fff" stroke-width="1.4" opacity=".7"/></svg>
      <div class="t title">CHECK IN</div>
      <div class="done">DONE</div>
    </div>
    <div class="photo" role="img" aria-label="Portrait photo of the client" style="left:84px;top:94px;width:136px;height:137px"></div>
    <div class="t heading" style="top:256px">30 Oct 2018 14:30:34 h</div>
    <div class="t heading" style="top:276px">Voluntary Check in Request</div>
    <div class="rule" style="left:66px;width:183px;top:304px"></div>
    <div class="t heading" style="top:315px;font-size:13.5px">Please Check in and</div>
    <div class="t heading" style="top:329px;font-size:13.5px">Quote this number:</div>
    <div class="t code" style="top:353px">C96H</div>
    <div class="t field-label" style="top:392px">CODE</div>
    <div class="rule" style="left:66px;width:183px;top:414px"></div>
    <div class="t heading" style="top:426px;font-size:13.5px">Comment:</div>
    <div class="t field-label" style="top:460px">TYPE OR REPLY</div>
    <div class="rule" style="left:66px;width:183px;top:484px"></div>
  </section>

  <!-- Info / profile -->
  <section class="screen info" style="left:103px;top:637px">
    <div class="band" style="height:169px"></div>
    <div class="header">
      <svg class="back" width="20" height="14" viewBox="0 0 20 14"><path d="M19 7H2M8 1L2 7l6 6" fill="none" stroke="#fff" stroke-width="1.4" opacity=".7"/></svg>
      <div class="t title">INFO</div>
      <div class="done">DONE</div>
    </div>
    <div class="photo" role="img" aria-label="Portrait photo of the client" style="left:83px;top:82px;width:139px;height:138px"></div>
    <div class="t person-name" style="top:245px">DALE HARMON</div>
    <div class="t person-address" style="top:273px">418 Larkspur Ave, Fenwick, OR 97310</div>
    <div class="row" style="left:40px;width:230px;top:327px"><span class="k">Email</span><span class="v">dale.harmon@mailbox.example</span></div>
    <div class="rule" style="left:40px;width:230px;top:350px"></div>
    <div class="row" style="left:40px;width:230px;top:363px"><span class="k">Password</span><span class="v" style="letter-spacing:1px">•••••••••••</span></div>
    <div class="rule" style="left:40px;width:230px;top:386px"></div>
    <div class="row" style="left:40px;width:104px;top:399px"><span class="k">Grander</span><span class="v">Male</span></div>
    <div class="row" style="left:174px;width:96px;top:399px"><span class="k">Age</span><span class="v">54</span></div>
    <div class="rule" style="left:40px;width:104px;top:422px"></div>
    <div class="rule" style="left:169px;width:101px;top:422px"></div>
    <div class="row" style="left:40px;width:230px;top:435px"><span class="k">Phone</span><span class="v">5550 - 13842</span></div>
    <div class="rule" style="left:40px;width:230px;top:458px"></div>
    <nav class="tabbar">
      <div class="tab" style="left:47px"><svg width="22" height="22" viewBox="0 0 22 22" fill="none" stroke="currentColor" stroke-width="1.1"><path d="M3 10L11 3l8 7M5 9v11h12V9M9 20v-6h4v6"/></svg>HOME</div>
      <div class="tab" style="left:112px"><svg width="22" height="22" viewBox="0 0 22 22" fill="none" stroke="currentColor" stroke-width="1.1"><path d="M11 21s-7-7-7-12a7 7 0 0 1 14 0c0 5-7 12-7 12z"/><circle cx="11" cy="9" r="4"/></svg>CHECK IN</div>
      <div class="tab" style="left:186px"><svg width="22" height="22" viewBox="0 0 22 22" fill="none" stroke="currentColor" stroke-width="1.1"><path d="M2 20l4-8h10l4 8zM8 12l-2 8M14 12l2 8"/><path d="M11 14s-4-4-4-7a4 4 0 0 1 8 0c0 3-4 7-4 7z"/></svg>MAP</div>
      <div class="tab active" style="left:253px"><svg width="22" height="22" viewBox="0 0 22 22" fill="none" stroke="currentColor" stroke-width="1.2"><circle cx="11" cy="11" r="9.5"/><path d="M11 9v7M9 16h4M9.5 9H11"/><circle cx="11" cy="6" r=".8" fill="currentColor"/></svg>INFO</div>
    </nav>
  </section>

  <!-- Check in list -->
  <section class="screen checkin-list" style="left:448px;top:637px">
    <div class="header">
      <svg class="back" width="20" height="14" viewBox="0 0 20 14"><path d="M19 7H2M8 1L2 7l6 6" fill="none" stroke="#fff" stroke-width="1.4" opacity=".7"/></svg>
      <div class="t title">CHECK IN</div>
    </div>
    <div class="entry" style="top:98px"><div class="date">30 Oct 2018 14:30:34 h</div><div class="kind">Voluntary Check in Request</div><span class="box" style="background:var(--brand)"></span></div>
    <div class="rule" style="left:48px;width:182px;top:146px"></div>
    <div class="entry" style="top:159px"><div class="date">30 Oct 2018 14:30:34 h</div><div class="kind">Voluntary Check in Request</div><span class="box" style="background:var(--alert)"></span></div>
    <div class="rule" style="left:48px;width:182px;top:208px"></div>
    <div class="entry" style="top:220px"><div class="date">30 Oct 2018 14:30:34 h</div><div class="kind">Voluntary Check in Request</div><span class="box" style="background:var(--ok)"></span></div>
    <div class="rule" style="left:48px;width:182px;top:268px"></div>
    <div class="entry" style="top:280px"><div class="date">30 Oct 2018 14:30:34 h</div><div class="kind">Voluntary Check in Request</div><span class="box" style="background:var(--ok)"></span></div>
    <div class="rule" style="left:48px;width:182px;top:328px"></div>
    <div class="entry" style="top:340px"><div class="date">30 Oct 2018 14:30:34 h</div><div class="kind">Voluntary Check in Request</div><span class="box" style="background:var(--ok)"></span></div>
    <div class="rule" style="left:48px;width:182px;top:389px"></div>
    <div class="entry" style="top:401px"><div class="date">30 Oct 2018 14:30:34 h</div><div class="kind">Voluntary Check in Request</div><span class="box" style="background:var(--ok)"></span></div>
    <div class="rule" style="left:48px;width:182px;top:449px"></div>
    <nav class="tabbar">
      <div class="tab" style="left:47px"><svg width="22" height="22" viewBox="0 0 22 22" fill="none" stroke="currentColor" stroke-width="1.1"><path d="M3 10L11 3l8 7M5 9v11h12V9M9 20v-6h4v6"/></svg>HOME</div>
      <div class="tab active" style="left:112px"><svg width="22" height="22" viewBox="0 0 22 22" fill="none" stroke="currentColor" stroke-width="1.2"><path d="M11 21s-7-7-7-12a7 7 0 0 1 14 0c0 5-7 12-7 12z"/><circle cx="11" cy="9" r="4"/></svg>CHECK IN</div>
      <div class="tab" style="left:186px"><svg width="22" height="22" viewBox="0 0 22 22" fill="none" stroke="currentColor" stroke-width="1.1"><path d="M2 20l4-8h10l4 8zM8 12l-2 8M14 12l2 8"/><path d="M11 14s-4-4-4-7a4 4 0 0 1 8 0c0 3-4 7-4 7z"/></svg>MAP</div>
      <div class="tab" style="left:253px"><svg width="22" height="22" viewBox="0 0 22 22" fill="none" stroke="currentColor" stroke-width="1.1"><circle cx="11" cy="11" r="9.5"/><path d="M11 9v7M9 16h4M9.5 9H11"/><circle cx="11" cy="6" r=".8" fill="currentColor"/></svg>INFO</div>
    </nav>
  </section>

  <!-- Home -->
  <section class="screen home" style="left:793px;top:637px">
    <div class="header">
      <svg class="back" width="20" height="14" viewBox="0 0 20 14"><path d="M19 7H2M8 1L2 7l6 6" fill="none" stroke="#fff" stroke-width="1.4" opacity=".7"/></svg>
      <div class="t title">HOME</div>
      <div class="done">DONE</div>
    </div>
    <div class="photo" role="img" aria-label="Portrait photo of the client" style="left:109px;top:138px;width:97px;height:97px;border-radius:12px"></div>
    <div class="t person-name" style="top:257px">DALE HARMON</div>
    <div class="rule" style="left:68px;width:183px;top:302px;background:rgba(255,255,255,.8)"></div>

    <div class="tile" style="left:82px;top:342px"><svg width="24" height="26" viewBox="0 0 24 26" fill="none" stroke="#fff" stroke-width="1.1"><path d="M12 25s-9-8-9-14a9 9 0 0 1 18 0c0 6-9 14-9 14z"/><circle cx="12" cy="11" r="5"/></svg>CHECK IN</div>
    <div class="tile" style="left:155px;top:342px"><svg width="28" height="26" viewBox="0 0 28 26" fill="none" stroke="#fff" stroke-width="1.1"><path d="M2 24l5-10h14l5 10zM10 14l-2 10M18 14l2 10"/><path d="M14 17s-5-5-5-9a5 5 0 0 1 10 0c0 4-5 9-5 9z"/></svg>MAP</div>
    <div class="tile" style="left:230px;top:342px"><svg width="34" height="26" viewBox="0 0 34 26" fill="none" stroke="#fff" stroke-width="1.6"><path d="M13 5a6 6 0 0 1 8 0M15 8a3 3 0 0 1 4 0"/><ellipse cx="17" cy="18" rx="15" ry="5" fill="#fff"/><rect x="9" y="12" width="16" height="5" rx="2" fill="#3277b5"/></svg>BARACELET</div>

    <div class="tile" style="left:82px;top:421px"><svg width="28" height="26" viewBox="0 0 28 26" fill="none" stroke="#fff" stroke-width="1.1"><path d="M3 24h22M5 24v-7h3v7M10 24V12h3v12M15 24v-9h3v9M20 24v-5h3v5M3 14l7-8 5 5 4-5 5 3"/></svg>STATISTIC</div>
    <div class="tile" style="left:155px;top:421px"><svg width="26" height="26" viewBox="0 0 26 26" fill="none" stroke="#fff" stroke-width="1.1"><circle cx="13" cy="13" r="11.5"/><circle cx="13" cy="10" r="4.5"/><path d="M5.5 21.5c1.5-4 4.5-6 7.5-6s6 2 7.5 6"/></svg>PROFIL</div>
    <div class="tile" style="left:230px;top:421px"><svg width="26" height="26" viewBox="0 0 26 26" fill="none" stroke="#fff" stroke-width="1.1"><circle cx="13" cy="13" r="11.5"/><path d="M13 11v8M11 19h4M11.5 11H13"/><circle cx="13" cy="7.5" r=".9" fill="#fff"/></svg>INFO</div>
  </section>

</div>
</body>
</html>
```